Ebook cover for the trade gateway handbook

I am publishing an ebook (zRead) called the trade gateway handbook
This is an ebook about how to pick a foreign market to sell your american products, how to enter that market correctly, and how to compare one country to another. The toolkit is multi media and uses articles, audio, video, digital spreadsheets. It will cost $99. It is more a toolkit that a book

the logo must be designed in "vector" so that it can be repurposed later if needed

the contents of the ebook can be found at www.tradegatewayhandbook.example you can also see a video there explaining the toolkit
Updates

Project Deadline Extended
Reason: Some of the designs are really good. It's hard to decide

Target Market(s)

Corporate executives who want to market their firms overseas

Industry/Entity Type

Digital

Logo Text

The Trade Gateway Handbook

Logo styles of interest
Pictorial/Combination Logo
Requirements
Must have
• Professional looking. Must fit in with corporate culture and look and Feel Of parent company.www.veltroglobalgroup.example
Nice to have
• Maroon and grey colors

```html
<!DOCTYPE html>
<html lang="en">
<head>
<meta charset="utf-8">
<title>The Trade Gateway Handbook — Cover Wraps</title>
<link rel="stylesheet" href="https://fonts.googleapis.com/css2?family=Arimo:wght@400;700&display=swap">
<style>
  :root {
    --maroon: #7a1530;
    --grey: #a7a9ac;
    --black: #0d0d0d;
    --white: #ffffff;
    --ink: #111111;
  }
  * { box-sizing: border-box; margin: 0; padding: 0; }
  html, body {
    width: 830px; height: 1200px; overflow: hidden;
    background: var(--white);
  }
  body { position: relative; font-family: "Arimo", Arial, sans-serif; color: var(--ink); }

  .wrap {
    position: absolute; left: 0; width: 830px; height: 596px;
    display: flex; overflow: hidden;
  }
  .wrap--grey { top: 0; }
  .wrap--light { top: 604px; }

  /* Back cover */
  .back {
    position: relative; width: 395px; height: 100%;
    background: var(--grey); overflow: hidden;
  }
  .wrap--light .back { background: var(--white); }
  .back__headline {
    position: absolute; top: 22px; left: 0; width: 100%;
    text-align: center; font-weight: 700; font-size: 24px; line-height: 29px;
  }
  .back__questions {
    position: absolute; top: 124px; left: 16px; right: 44px;
    list-style: none; font-size: 14px; line-height: 19px; font-weight: 700;
  }
  .back__questions li { position: relative; padding-left: 14px; margin-bottom: 4px; }
  .back__questions li::before {
    content: ""; position: absolute; left: 0; top: 7px;
    width: 4px; height: 4px; background: var(--maroon);
  }
  .wrap--light .back__questions li::before { background: var(--ink); }
  .back__bar { position: absolute; right: 0; background: var(--maroon); }
  .back__bar--wide  { top: 340px; left: 8px;  height: 38px; }
  .back__bar--one   { top: 395px; left: 146px; height: 28px; }
  .back__bar--two   { top: 438px; left: 45px;  height: 33px; }
  .back__bar--three { top: 486px; left: 146px; height: 39px; }
  .back__url {
    position: absolute; top: 538px; left: 0; width: 100%;
    text-align: center; font-weight: 700; font-size: 19px;
  }

  /* Spine */
  .spine {
    flex: 0 0 43px; width: 43px; height: 100%; background: var(--black);
    display: flex; align-items: flex-start; justify-content: center;
    border-right: 6px solid var(--maroon);
  }
  .wrap--light .spine { border-right-color: var(--black); }
  .spine__title {
    writing-mode: vertical-rl; margin-top: 22px;
    font-weight: 700; font-size: 21px; letter-spacing: 0.5px;
    color: var(--maroon); white-space: nowrap;
  }
  .wrap--light .spine__title { color: var(--white); }

  /* Front cover */
  .front {
    position: relative; flex: 1; height: 100%; min-width: 0;
    background: var(--grey); overflow: hidden;
  }
  .wrap--light .front { background: var(--white); }
  .front__title { position: absolute; top: 22px; left: 14px; right: 0; }
  .front__line {
    display: flex; align-items: center; height: 48px;
    font-weight: 700; font-size: 54px; line-height: 1; color: var(--maroon);
    letter-spacing: -0.5px; white-space: nowrap;
  }
  .front__line-bar { flex: 1; height: 38px; margin-left: 12px; background: var(--maroon); }
  .front__band { position: absolute; left: 0; right: 0; background: var(--black); }
  .front__band--top { top: 226px; height: 30px; }
  .front__band--bottom { top: 508px; height: 14px; }
  .front__feature {
    position: absolute; top: 256px; left: 0; right: 0; height: 252px;
    background: var(--maroon); display: flex; align-items: center; justify-content: center;
  }
  .wrap--light .front__feature { background: var(--white); }
  .front__photo {
    width: 300px; height: 200px;
    background: linear-gradient(135deg, #e9e9ea 0%, #c9c9cc 55%, #4a4a4c 100%);
  }
  .front__author {
    position: absolute; top: 538px; left: 0; width: 100%;
    text-align: center; font-weight: 700; font-size: 34px; color: var(--maroon);
  }
</style>
</head>
<body>

<section class="wrap wrap--grey">
  <div class="back">
    <h2 class="back__headline">Use the Toolkit,<br>and do it<br>Right the First Time</h2>
    <ul class="back__questions">
      <li>How do you choose a foreign market correctly?</li>
      <li>How do you get your company into a foreign market?</li>
      <li>How do you effectively sell overseas?</li>
      <li>How do you avoid the losing your shirt abroad?</li>
      <li>How do you explain to your firm that you have chosen the correct markets?</li>
      <li>Could your venture could be more successful abroad than in the USA?</li>
    </ul>
    <div class="back__bar back__bar--wide"></div>
    <div class="back__bar back__bar--one"></div>
    <div class="back__bar back__bar--two"></div>
    <div class="back__bar back__bar--three"></div>
    <p class="back__url">www.tradegatewayhandbook.example</p>
  </div>
  <div class="spine"><span class="spine__title">The Trade Gateway Handbook</span></div>
  <div class="front">
    <h1 class="front__title">
      <span class="front__line">THE<span class="front__line-bar"></span></span>
      <span class="front__line">TRADE<span class="front__line-bar"></span></span>
      <span class="front__line">GATEWAY<span class="front__line-bar"></span></span>
      <span class="front__line">HANDBOOK<span class="front__line-bar"></span></span>
    </h1>
    <div class="front__band front__band--top"></div>
    <div class="front__feature">
      <div class="front__photo" role="img" aria-label="Photo of a black briefcase with printed handbook pages and a CD in a case"></div>
    </div>
    <div class="front__band front__band--bottom"></div>
    <p class="front__author">By Dale Whitmore</p>
  </div>
</section>

<section class="wrap wrap--light">
  <div class="back">
    <h2 class="back__headline">Use the Toolkit,<br>and do it<br>Right the First Time</h2>
    <ul class="back__questions">
      <li>How do you choose a foreign market correctly?</li>
      <li>How do you get your company into a foreign market?</li>
      <li>How do you effectively sell overseas?</li>
      <li>How do you avoid the losing your shirt abroad?</li>
      <li>How do you explain to your firm that you have chosen the correct markets?</li>
      <li>Could your venture could be more successful abroad than in the USA?</li>
    </ul>
    <div class="back__bar back__bar--wide"></div>
    <div class="back__bar back__bar--one"></div>
    <div class="back__bar back__bar--two"></div>
    <div class="back__bar back__bar--three"></div>
    <p class="back__url">www.tradegatewayhandbook.example</p>
  </div>
  <div class="spine"><span class="spine__title">The Trade Gateway Handbook</span></div>
  <div class="front">
    <h1 class="front__title">
      <span class="front__line">THE<span class="front__line-bar"></span></span>
      <span class="front__line">TRADE<span class="front__line-bar"></span></span>
      <span class="front__line">GATEWAY<span class="front__line-bar"></span></span>
      <span class="front__line">HANDBOOK<span class="front__line-bar"></span></span>
    </h1>
    <div class="front__band front__band--top"></div>
    <div class="front__feature">
      <div class="front__photo" role="img" aria-label="Photo of a black briefcase with printed handbook pages and a CD in a case"></div>
    </div>
    <div class="front__band front__band--bottom"></div>
    <p class="front__author">By Dale Whitmore</p>
  </div>
</section>

</body>
</html>
```